How likely are people to engage in social distancing? We need a good illustration to show the data!

We surveyed U.S. adults March 20th - 24th, 2020 and asked how likely they were to engage in social distancing (and other COVID-19 related health behaviors). What did the survey find? Basically, most people intend to engage in social distancing behaviors (e.g., avoiding large crowds) and other behaviors that reduce the spread of COVID-19 (e.g., washing hands at least 20 seconds). When most people intend to engage in a behavior, then public health professionals try to leverage that to move more people to act.
Now we need innovative and professional images that attempt to communicate one or all of these findings. The specific findings are nicely summarized in the attached document. For example, 82% of participants intend to engage in social distancing.
What sort of visual are we looking for? Our preference is for an original illustration (or set of illustrations). Our preference is for (creative and powerful illustrations, but we are also open to the creative and well-executed infographics.
We need these images fast . We will award monetary prizes to the 3 best designs. If we like more than that, then we might purchase more (e.g., in past contests, we have purchased as many as 30 designs).
What we will need:
(1) The illustrations must be original and we will need the photoshop and/or illustrator files for all artwork.
(2) You can illustrate all of the findings or just one of them. We need creative approaches that do a lucid job of bringing the data to life. Most people intend to engage in these behaviors. How to communicate that? Corvantists and Halmerites do not differ in their intentions; how to communicate that?
(3) The illustration should say, somewhere: "Based on a survey of 400 U.S. adults conducted March 20 - 24th, 2020."

U.S. Adults

• Original illustrations based on the findings of the survey (see attached document).

```html
<!DOCTYPE html>
<html lang="en">
<head>
<meta charset="utf-8">
<title>Survey of U.S. Adults – Social Distancing Intentions</title>
<link rel="stylesheet" href="https://fonts.googleapis.com/css2?family=Arvo:wght@700&family=Roboto:wght@400;500;700&family=Roboto+Condensed:wght@400&family=Nunito:wght@900&display=swap">
<style>
  :root {
    --bg: #3e1029;
    --bg-deep: #2f0a1e;
    --white: #ffffff;
    --card-top: #9c2a64;
    --card-bottom: #e3c5d3;
    --pie-top: #9b1e5f;
    --pie-side: #5e1840;
    --pie-gray: #c9c9c9;
    --pie-gray-side: #7b7b7b;
    --corv-face: #d42f96;
    --corv-side: #8a1d5e;
    --halm-side: #2a2460;
    --halm-face: #4a3fbf;
    --axis-label: #e6e6e6;
  }
  * { margin: 0; padding: 0; box-sizing: border-box; }
  html, body { width: 1200px; height: 2201px; overflow: hidden; }
  body {
    position: relative;
    background: radial-gradient(ellipse at 30% 20%, #4a1532 0%, var(--bg) 45%, var(--bg-deep) 100%);
    color: var(--white);
    font-family: "Roboto", Arial, sans-serif;
  }
  .title {
    position: absolute; top: 40px; left: 0; width: 1200px;
    text-align: center; font-family: "Arvo", Georgia, serif; font-weight: 700;
    font-size: 51px; line-height: 60px;
  }
  .subtitle {
    position: absolute; top: 184px; left: 0; width: 1200px;
    text-align: center; font-size: 34px; font-weight: 400;
  }
  .rule { position: absolute; background: var(--white); }
  .rule.top { left: 50px; top: 269px; width: 1101px; height: 3px; }
  .question {
    position: absolute; top: 332px; left: 0; width: 1200px;
    text-align: center; font-weight: 700; font-size: 33px; line-height: 48px;
    letter-spacing: 0.5px;
  }
  .card {
    position: absolute; width: 244px; height: 359px; border-radius: 40px;
    background: linear-gradient(180deg, var(--card-top) 0%, #b96f92 45%, var(--card-bottom) 80%, var(--card-bottom) 100%);
    overflow: hidden;
  }
  .card-title {
    position: absolute; top: 9px; left: 0; width: 100%;
    text-align: center; font-family: "Arvo", Georgia, serif; font-weight: 700;
    font-size: 23px; line-height: 28px; letter-spacing: 0.5px;
  }
  .card-title.small { font-size: 18px; line-height: 23px; top: 14px; }
  .card-title.mid { font-size: 20px; line-height: 25px; top: 9px; }
  .art {
    position: absolute; left: 32px; right: 32px; top: 72px; height: 118px;
    border-radius: 14px;
    background: linear-gradient(180deg, rgba(255,255,255,0.16), rgba(60,10,40,0.14));
  }
  .row2 .art { top: 78px; height: 122px; }
  .pie { position: absolute; left: 0; top: 0; width: 244px; height: 359px; }
  .pct { font-family: "Nunito", Arial, sans-serif; font-weight: 900; font-size: 43px; }
  .compare-title {
    position: absolute; top: 1280px; left: 0; width: 1200px;
    text-align: center; font-weight: 500; font-size: 44px; letter-spacing: 0.5px;
  }
  .compare-sub {
    position: absolute; top: 1337px; left: 0; width: 1200px;
    text-align: center; font-size: 34px;
  }
  .rule.side-l { left: 49px; top: 1305px; width: 96px; height: 2px; }
  .rule.side-r { left: 1056px; top: 1305px; width: 95px; height: 2px; }
  .rule.under { left: 342px; top: 1392px; width: 510px; height: 4px; }
  .chart { position: absolute; left: 0; top: 0; width: 1200px; height: 2201px; }
  .tick-label { font-family: "Roboto", Arial, sans-serif; font-weight: 700; font-size: 27px; fill: var(--white); }
  .bar-val { font-family: "Roboto", Arial, sans-serif; font-style: italic; font-weight: 500; font-size: 15px; fill: var(--white); }
  .cat { font-family: "Roboto Condensed", Arial, sans-serif; font-size: 21px; fill: var(--axis-label); }
  .cat.sm { font-size: 17px; }
  .legend-label { font-family: "Roboto", Arial, sans-serif; font-size: 23px; fill: var(--white); }
  .footnote {
    position: absolute; top: 2116px; left: 0; width: 1200px;
    text-align: center; font-size: 22px;
  }
</style>
</head>
<body>
  <h1 class="title">Survey of U.S. Adults (N = 400)<br>conducted March 20th - 24th, 2020</h1>
  <p class="subtitle">Percent of Americans intending to engage in social distancing</p>
  <div class="rule top"></div>
  <p class="question">We would like to know how likely it is that you will perform<br>these behaviors to slow the spread of coronavirus?</p>

  <!-- Row 1 -->
  <div class="card" style="left:49px; top:462px;">
    <div class="card-title">Engage in<br>Social Distancing</div>
    <div class="art" role="img" aria-label="Three figures standing six feet apart with arrows between them"></div>
    <svg class="pie" viewBox="0 0 244 359">
      <path d="M17 256 A105 58 0 0 0 227 256 L227 290 A105 58 0 0 1 17 290 Z" fill="var(--pie-side)"/>
      <path d="M122 314 A105 58 0 0 1 27 280.7 L27 314.7 A105 58 0 0 0 122 348 Z" fill="var(--pie-gray-side)"/>
      <ellipse cx="122" cy="256" rx="105" ry="58" fill="var(--pie-top)"/>
      <path d="M122 256 L122 314 A105 58 0 0 1 27 280.7 Z" fill="var(--pie-gray)"/>
      <text class="pct" x="138" y="249" text-anchor="middle" fill="#8d8d8d">82%</text>
      <text class="pct" x="135" y="246" text-anchor="middle" fill="#fff">82%</text>
    </svg>
  </div>

  <div class="card" style="left:335px; top:462px;">
    <div class="card-title">Work from<br>Home</div>
    <div class="art" role="img" aria-label="Person working on a laptop at a desk with a lamp and a mug"></div>
    <svg class="pie" viewBox="0 0 244 359">
      <path d="M17 256 A105 58 0 0 0 227 256 L227 290 A105 58 0 0 1 17 290 Z" fill="var(--pie-side)"/>
      <path d="M122 314 A105 58 0 0 1 17 256 L17 290 A105 58 0 0 0 122 348 Z" fill="var(--pie-gray-side)"/>
      <ellipse cx="122" cy="256" rx="105" ry="58" fill="var(--pie-top)"/>
      <path d="M122 256 L122 314 A105 58 0 0 1 45.5 216.3 Z" fill="var(--pie-gray)"/>
      <text class="pct" x="128" y="249" text-anchor="middle" fill="#8d8d8d">63%</text>
      <text class="pct" x="125" y="246" text-anchor="middle" fill="#fff">63%</text>
    </svg>
  </div>

  <div class="card" style="left:620px; top:462px;">
    <div class="card-title">Avoid Large<br>Gatherings</div>
    <div class="art" role="img" aria-label="Dense crowd of small figures"></div>
    <svg class="pie" viewBox="0 0 244 359">
      <path d="M17 256 A105 58 0 0 0 227 256 L227 290 A105 58 0 0 1 17 290 Z" fill="var(--pie-side)"/>
      <path d="M122 314 A105 58 0 0 1 37.1 290.1 L37.1 324.1 A105 58 0 0 0 122 348 Z" fill="var(--pie-gray-side)"/>
      <ellipse cx="122" cy="256" rx="105" ry="58" fill="var(--pie-top)"/>
      <path d="M122 256 L122 314 A105 58 0 0 1 37.1 290.1 Z" fill="var(--pie-gray)"/>
      <text class="pct" x="138" y="249" text-anchor="middle" fill="#8d8d8d">85%</text>
      <text class="pct" x="135" y="246" text-anchor="middle" fill="#fff">85%</text>
    </svg>
  </div>

  <div class="card" style="left:906px; top:462px;">
    <div class="card-title">Cancel<br>Social Activities</div>
    <div class="art" role="img" aria-label="Group of four friends standing arm in arm, seen from behind"></div>
    <svg class="pie" viewBox="0 0 244 359">
      <path d="M17 256 A105 58 0 0 0 227 256 L227 290 A105 58 0 0 1 17 290 Z" fill="var(--pie-side)"/>
      <path d="M122 314 A105 58 0 0 1 24.4 277.3 L24.4 311.3 A105 58 0 0 0 122 348 Z" fill="var(--pie-gray-side)"/>
      <ellipse cx="122" cy="256" rx="105" ry="58" fill="var(--pie-top)"/>
      <path d="M122 256 L122 314 A105 58 0 0 1 24.4 277.3 Z" fill="var(--pie-gray)"/>
      <text class="pct" x="138" y="249" text-anchor="middle" fill="#8d8d8d">81%</text>
      <text class="pct" x="135" y="246" text-anchor="middle" fill="#fff">81%</text>
    </svg>
  </div>

  <!-- Row 2 -->
  <div class="card row2" style="left:49px; top:867px;">
    <div class="card-title small">Put distance between<br>yourself &amp; others</div>
    <div class="art" role="img" aria-label="Small group of figures kept six feet away from a single figure"></div>
    <svg class="pie" viewBox="0 0 244 359">
      <path d="M17 256 A105 58 0 0 0 227 256 L227 290 A105 58 0 0 1 17 290 Z" fill="var(--pie-side)"/>
      <path d="M122 314 A105 58 0 0 1 37.1 290.1 L37.1 324.1 A105 58 0 0 0 122 348 Z" fill="var(--pie-gray-side)"/>
      <ellipse cx="122" cy="256" rx="105" ry="58" fill="var(--pie-top)"/>
      <path d="M122 256 L122 314 A105 58 0 0 1 37.1 290.1 Z" fill="var(--pie-gray)"/>
      <text class="pct" x="133" y="249" text-anchor="middle" fill="#8d8d8d">85%</text>
      <text class="pct" x="130" y="246" text-anchor="middle" fill="#fff">85%</text>
    </svg>
  </div>

  <div class="card row2" style="left:335px; top:867px;">
    <div class="card-title">Wash Hands<br>atleast 20 Sec</div>
    <div class="art" role="img" aria-label="Two hands lathering with soap bubbles"></div>
    <svg class="pie" viewBox="0 0 244 359">
      <path d="M17 256 A105 58 0 0 0 227 256 L227 290 A105 58 0 0 1 17 290 Z" fill="var(--pie-side)"/>
      <path d="M122 314 A105 58 0 0 1 45.5 295.7 L45.5 329.7 A105 58 0 0 0 122 348 Z" fill="var(--pie-gray-side)"/>
      <ellipse cx="122" cy="256" rx="105" ry="58" fill="var(--pie-top)"/>
      <path d="M122 256 L122 314 A105 58 0 0 1 45.5 295.7 Z" fill="var(--pie-gray)"/>
      <text class="pct" x="131" y="249" text-anchor="middle" fill="#8d8d8d">87%</text>
      <text class="pct" x="128" y="246" text-anchor="middle" fill="#fff">87%</text>
    </svg>
  </div>

  <div class="card row2" style="left:620px; top:867px;">
    <div class="card-title">Use<br>Hand Sanitizers</div>
    <div class="art" role="img" aria-label="Pump bottle of hand sanitizer with a red cross label"></div>
    <svg class="pie" viewBox="0 0 244 359">
      <path d="M17 256 A105 58 0 0 0 227 256 L227 290 A105 58 0 0 1 17 290 Z" fill="var(--pie-side)"/>
      <path d="M122 314 A105 58 0 0 1 37.1 290.1 L37.1 324.1 A105 58 0 0 0 122 348 Z" fill="var(--pie-gray-side)"/>
      <ellipse cx="122" cy="256" rx="105" ry="58" fill="var(--pie-top)"/>
      <path d="M122 256 L122 314 A105 58 0 0 1 37.1 290.1 Z" fill="var(--pie-gray)"/>
      <text class="pct" x="138" y="249" text-anchor="middle" fill="#8d8d8d">85%</text>
      <text class="pct" x="135" y="246" text-anchor="middle" fill="#fff">85%</text>
    </svg>
  </div>

  <div class="card row2" style="left:906px; top:867px;">
    <div class="card-title mid">Avoid touching<br>Eyes, Nose &amp; Mouth</div>
    <div class="art" role="img" aria-label="Prohibition sign over a nose, lips and an eye"></div>
    <svg class="pie" viewBox="0 0 244 359">
      <path d="M17 256 A105 58 0 0 0 227 256 L227 290 A105 58 0 0 1 17 290 Z" fill="var(--pie-side)"/>
      <path d="M122 314 A105 58 0 0 1 24.4 277.3 L24.4 311.3 A105 58 0 0 0 122 348 Z" fill="var(--pie-gray-side)"/>
      <ellipse cx="122" cy="256" rx="105" ry="58" fill="var(--pie-top)"/>
      <path d="M122 256 L122 314 A105 58 0 0 1 24.4 277.3 Z" fill="var(--pie-gray)"/>
      <text class="pct" x="138" y="249" text-anchor="middle" fill="#8d8d8d">81%</text>
      <text class="pct" x="135" y="246" text-anchor="middle" fill="#fff">81%</text>
    </svg>
  </div>

  <!-- Comparison -->
  <div class="rule side-l"></div>
  <div class="rule side-r"></div>
  <h2 class="compare-title">Comparing Corvantists and Halmerites</h2>
  <p class="compare-sub">March 20th - 24th, 2020 Survey</p>
  <div class="rule under"></div>

  <svg class="chart" viewBox="0 0 1200 2201">
    <!-- axes -->
    <g stroke="#fff" stroke-width="3" fill="none">
      <polyline points="182,1446 143,1446 143,1933 1115,1933 1115,1918"/>
      <line x1="143" y1="1543.5" x2="167" y2="1543.5"/>
      <line x1="143" y1="1641" x2="167" y2="1641"/>
      <line x1="143" y1="1738" x2="167" y2="1738"/>
      <line x1="143" y1="1836" x2="167" y2="1836"/>
      <line x1="276" y1="1933" x2="276" y2="1948"/>
      <line x1="396" y1="1933" x2="396" y2="1948"/>
      <line x1="515" y1="1933" x2="515" y2="1948"/>
      <line x1="635" y1="1933" x2="635" y2="1948"/>
      <line x1="755" y1="1933" x2="755" y2="1948"/>
      <line x1="874" y1="1933" x2="874" y2="1948"/>
      <line x1="994" y1="1933" x2="994" y2="1948"/>
    </g>
    <g class="tick-label" text-anchor="end">
      <text x="128" y="1457">100%</text>
      <text x="128" y="1554">80%</text>
      <text x="128" y="1652">60%</text>
      <text x="128" y="1749">40%</text>
      <text x="128" y="1847">20%</text>
      <text x="128" y="1944">0%</text>
    </g>

    <!-- group: social distancing 82 / 81 -->
    <g transform="translate(161,0)">
      <polygon points="62,1540 91,1532 91,1933 62,1933" fill="var(--halm-side)"/>
      <polygon points="91,1532 118,1542 118,1933 91,1933" fill="var(--halm-face)"/>
      <polygon points="0,1538 36,1528 36,1933 0,1933" fill="var(--corv-face)"/>
      <polygon points="36,1528 66,1536 66,1933 36,1933" fill="var(--corv-side)"/>
      <text class="bar-val" transform="translate(4,1556) rotate(18)">82%</text>
      <text class="bar-val" transform="translate(93,1562) rotate(-18)">81%</text>
    </g>
    <!-- work from home 60 / 65 -->
    <g transform="translate(280,0)">
      <polygon points="62,1619 91,1611 91,1933 62,1933" fill="var(--halm-side)"/>
      <polygon points="91,1611 118,1621 118,1933 91,1933" fill="var(--halm-face)"/>
      <polygon points="0,1645 36,1635 36,1933 0,1933" fill="var(--corv-face)"/>
      <polygon points="36,1635 66,1643 66,1933 36,1933" fill="var(--corv-side)"/>
      <text class="bar-val" transform="translate(4,1663) rotate(18)">60%</text>
      <text class="bar-val" transform="translate(93,1641) rotate(-18)">65%</text>
    </g>
    <!-- large gatherings 85 / 84 -->
    <g transform="translate(400,0)">
      <polygon points="62,1526 91,1518 91,1933 62,1933" fill="var(--halm-side)"/>
      <polygon points="91,1518 118,1528 118,1933 91,1933" fill="var(--halm-face)"/>
      <polygon points="0,1523 36,1513 36,1933 0,1933" fill="var(--corv-face)"/>
      <polygon points="36,1513 66,1521 66,1933 36,1933" fill="var(--corv-side)"/>
      <text class="bar-val" transform="translate(4,1541) rotate(18)">85%</text>
      <text class="bar-val" transform="translate(93,1548) rotate(-18)">84%</text>
    </g>
    <!-- cancel social 82 / 80 -->
    <g transform="translate(520,0)">
      <polygon points="62,1545 91,1537 91,1933 62,1933" fill="var(--halm-side)"/>
      <polygon points="91,1537 118,1547 118,1933 91,1933" fill="var(--halm-face)"/>
      <polygon points="0,1538 36,1528 36,1933 0,1933" fill="var(--corv-face)"/>
      <polygon points="36,1528 66,1536 66,1933 36,1933" fill="var(--corv-side)"/>
      <text class="bar-val" transform="translate(4,1556) rotate(18)">82%</text>
      <text class="bar-val" transform="translate(93,1567) rotate(-18)">80%</text>
    </g>
    <!-- put distance 84 / 87 -->
    <g transform="translate(639,0)">
      <polygon points="62,1511 91,1503 91,1933 62,1933" fill="var(--halm-side)"/>
      <polygon points="91,1503 118,1513 118,1933 91,1933" fill="var(--halm-face)"/>
      <polygon points="0,1528 36,1518 36,1933 0,1933" fill="var(--corv-face)"/>
      <polygon points="36,1518 66,1526 66,1933 36,1933" fill="var(--corv-side)"/>
      <text class="bar-val" transform="translate(4,1546) rotate(18)">84%</text>
      <text class="bar-val" transform="translate(93,1533) rotate(-18)">87%</text>
    </g>
    <!-- wash hands 87 / 88 -->
    <g transform="translate(759,0)">
      <polygon points="62,1506 91,1498 91,1933 62,1933" fill="var(--halm-side)"/>
      <polygon points="91,1498 118,1508 118,1933 91,1933" fill="var(--halm-face)"/>
      <polygon points="0,1513 36,1503 36,1933 0,1933" fill="var(--corv-face)"/>
      <polygon points="36,1503 66,1511 66,1933 36,1933" fill="var(--corv-side)"/>
      <text class="bar-val" transform="translate(4,1531) rotate(18)">87%</text>
      <text class="bar-val" transform="translate(93,1528) rotate(-18)">88%</text>
    </g>
    <!-- hand sanitizer 87 / 84 -->
    <g transform="translate(879,0)">
      <polygon points="62,1526 91,1518 91,1933 62,1933" fill="var(--halm-side)"/>
      <polygon points="91,1518 118,1528 118,1933 91,1933" fill="var(--halm-face)"/>
      <polygon points="0,1513 36,1503 36,1933 0,1933" fill="var(--corv-face)"/>
      <polygon points="36,1503 66,1511 66,1933 36,1933" fill="var(--corv-side)"/>
      <text class="bar-val" transform="translate(4,1531) rotate(18)">87%</text>
      <text class="bar-val" transform="translate(93,1548) rotate(-18)">84%</text>
    </g>
    <!-- avoid touching 80 / 82 -->
    <g transform="translate(998,0)">
      <polygon points="62,1536 91,1528 91,1933 62,1933" fill="var(--halm-side)"/>
      <polygon points="91,1528 118,1538 118,1933 91,1933" fill="var(--halm-face)"/>
      <polygon points="0,1547 36,1537 36,1933 0,1933" fill="var(--corv-face)"/>
      <polygon points="36,1537 66,1545 66,1933 36,1933" fill="var(--corv-side)"/>
      <text class="bar-val" transform="translate(4,1565) rotate(18)">80%</text>
      <text class="bar-val" transform="translate(93,1558) rotate(-18)">82%</text>
    </g>

    <!-- category labels -->
    <g text-anchor="middle">
      <text class="cat" x="212" y="1961">Engage in</text>
      <text class="cat" x="212" y="1982">social</text>
      <text class="cat" x="212" y="2003">distancing</text>
      <text class="cat" x="338" y="1961">Work from</text>
      <text class="cat" x="338" y="1982">home</text>
      <text class="cat" x="456" y="1961">Avoid large</text>
      <text class="cat" x="456" y="1982">gatherings</text>
      <text class="cat" x="576" y="1961">Cancel social</text>
      <text class="cat" x="576" y="1982">activities</text>
      <text class="cat sm" x="695" y="1958">Put distance</text>
      <text class="cat sm" x="695" y="1978">between yourself</text>
      <text class="cat sm" x="695" y="1998">and other people</text>
      <text class="cat" x="815" y="1961">Wash hands</text>
      <text class="cat" x="815" y="1982">atleast</text>
      <text class="cat" x="815" y="2003">20 seconds</text>
      <text class="cat" x="935" y="1961">Use hand</text>
      <text class="cat" x="935" y="1982">sanitizer</text>
      <text class="cat sm" x="1055" y="1958">Avoid touching</text>
      <text class="cat sm" x="1055" y="1978">your eyes, nose,</text>
      <text class="cat sm" x="1055" y="1998">and mouth</text>
    </g>

    <!-- legend -->
    <rect x="268" y="2044" width="65" height="26" fill="var(--corv-face)"/>
    <text class="legend-label" x="343" y="2065">Corvantist</text>
    <rect x="757" y="2044" width="65" height="26" fill="var(--halm-face)"/>
    <text class="legend-label" x="833" y="2065">Halmerite</text>
  </svg>

  <p class="footnote">*Based on a survey of 400 U.S. adults conducted March 20 – 24th, 2020.</p>
</body>
</html>
```